Commercial Loan Originator Business Card (CHANGE COLORS SCHEME)

CHANGE COLOR SCHEME - SAME DESIGN

Name Miranda Lestock
Title Commercial Loan Originator
Office (800) 641-2905 x68
Direct (240) 731-2264
Email gardenpath4life@mailbox.example

Name Dale Fenwick
Office (800) 641-2905 x70
Direct (410) 392-6058
Email d.fenwickhomes@mailbox.example

Name Gerald Winslow
Office (800) 641-2905 x71
Direct (215) 946-3021
Email g.winslow63@mailbox.example

Name Joan Mallory
Office (800) 641-2905 x
Direct (202) 518-4467
Email jmallory74@mailbox.example

Name Norah Velasco
Office (800) 641-2905 x72
Direct (240) 867-1152
Email capitalhomelending@mailbox.example

```html
<!DOCTYPE html>
<html lang="en">
<head>
<meta charset="utf-8">
<title>Miranda Lestock – Business Card</title>
<link rel="stylesheet" href="https://fonts.googleapis.com/css2?family=Poppins:wght@400;500;600&display=swap">
<style>
  :root {
    --page-bg: #3a3a3e;
    --card-white: #f7f7f8;
    --pink: #ec4aa0;
    --pink-deep: #d81c86;
    --pink-light: #f463b2;
    --swoosh-grey: #e4e3e7;
    --ink: #2d2d2f;
    --white: #ffffff;
  }
  * { margin: 0; padding: 0; box-sizing: border-box; }
  html, body {
    width: 1200px;
    height: 1200px;
    overflow: hidden;
    background: var(--page-bg);
    font-family: "Poppins", sans-serif;
  }
  .canvas {
    position: relative;
    width: 1200px;
    height: 1200px;
    display: flex;
    align-items: center;
    justify-content: center;
  }
  .business-card {
    position: relative;
    width: 1000px;
    height: 580px;
    border-radius: 26px;
    overflow: hidden;
    background: var(--card-white);
    box-shadow: 0 18px 40px rgba(0, 0, 0, 0.35);
  }
  .card-art {
    position: absolute;
    inset: 0;
    width: 100%;
    height: 100%;
  }
  .identity {
    position: absolute;
    left: 50px;
    top: 238px;
  }
  .identity-name {
    font-size: 46px;
    font-weight: 600;
    color: var(--pink);
    line-height: 1.1;
  }
  .identity-title {
    font-size: 24px;
    font-weight: 400;
    color: var(--ink);
    margin-top: 4px;
    letter-spacing: 0.2px;
  }
  .contact-list {
    position: absolute;
    left: 50px;
    bottom: 40px;
    list-style: none;
    color: var(--white);
    font-size: 26px;
    line-height: 40px;
  }
  .contact-label {
    font-weight: 600;
  }
  .contact-value {
    font-weight: 400;
  }
</style>
</head>
<body>
<main class="canvas">
  <section class="business-card">
    <svg class="card-art" viewBox="0 0 1000 580" aria-hidden="false">
      <defs>
        <linearGradient id="pinkBand" x1="0" y1="1" x2="1" y2="0">
          <stop offset="0" stop-color="var(--pink-light)"/>
          <stop offset="0.6" stop-color="var(--pink)"/>
          <stop offset="1" stop-color="var(--pink-deep)"/>
        </linearGradient>
        <linearGradient id="portraitTone" x1="0" y1="0" x2="0" y2="1">
          <stop offset="0" stop-color="#efeef0"/>
          <stop offset="0.55" stop-color="#d9b7a6"/>
          <stop offset="1" stop-color="#ec5aae"/>
        </linearGradient>
      </defs>

      <!-- grey swoosh behind portrait -->
      <path class="grey-swoosh" d="M520,330 C700,300 880,230 1000,120 L1000,260 C860,300 700,320 520,330 Z" fill="var(--swoosh-grey)"/>

      <!-- pink lower band -->
      <path class="pink-band" d="M0,410 C240,320 560,300 760,290 C870,284 950,260 1000,235 L1000,580 L0,580 Z" fill="url(#pinkBand)"/>

      <!-- thin white swoosh inside band -->
      <path class="white-swoosh" d="M600,305 C760,300 880,282 1000,248 L1000,258 C880,296 760,310 600,305 Z" fill="var(--white)"/>

      <!-- portrait frame -->
      <circle class="portrait-ring" cx="760" cy="152" r="128" fill="none" stroke="var(--pink)" stroke-width="2.5" stroke-dasharray="7 6"/>
      <circle class="portrait" cx="760" cy="152" r="116" fill="url(#portraitTone)" role="img" aria-label="Portrait photo of Miranda Lestock"/>
    </svg>

    <header class="identity">
      <h1 class="identity-name">Miranda Lestock</h1>
      <p class="identity-title">Commercial Loan Originator</p>
    </header>

    <ul class="contact-list">
      <li><span class="contact-label">Office:</span> <span class="contact-value">(800) 641-2905 x68</span></li>
      <li><span class="contact-label">Direct:</span> <span class="contact-value">(240) 731-2264</span></li>
      <li><span class="contact-label">Email:</span> <span class="contact-value">gardenpath4life@mailbox.example</span></li>
    </ul>
  </section>
</main>
</body>
</html>
```